Bold, Fun Hot Sauce Label

Hello,
We are a brand that are launching 4 new flavours of Hot Sauces in the next couple of months. We're looking for a label design that is just as fun & bold as these sauces with lots of colour & a modern look. It is a 3x5 label (attached) with 4 flavours:
1. Original Hot Sauce
2. Carolina Reaper Hot Sauce
3. Trinidad Scorpion Hot Sauce
4. Ghost Pepper Hot Sauce
Thank you

```html
<!DOCTYPE html>
<html lang="en">
<head>
<meta charset="UTF-8">
<title>Original Hot Sauce Label</title>
<link href="https://fonts.googleapis.com/css2?family=Archivo+Black&family=Archivo:wght@700&display=swap" rel="stylesheet">
<style>
  :root {
    --bg: #f4f4f5;
    --label: #f7f7f8;
    --red: #dc3a40;
    --red-deep: #b9262d;
    --pink: #f28a8f;
    --ink: #2a2a2a;
  }
  html, body {
    margin: 0;
    padding: 0;
    width: 1200px;
    height: 1200px;
    overflow: hidden;
    background: var(--bg);
  }
  .canvas {
    position: relative;
    width: 1200px;
    height: 1200px;
  }
  .label {
    position: absolute;
    left: 275px;
    top: 175px;
    width: 650px;
    height: 850px;
    background: var(--label);
    box-shadow: 0 6px 30px rgba(0,0,0,0.08);
    overflow: hidden;
  }
  .pepper-arc {
    position: absolute;
    left: 65px;
    top: 30px;
    width: 500px;
    height: 250px;
  }
  .title {
    position: absolute;
    left: 0;
    width: 100%;
    top: 310px;
    margin: 0;
    text-align: center;
    font-family: "Archivo Black", sans-serif;
    font-weight: 400;
    font-size: 78px;
    line-height: 112px;
    letter-spacing: -2px;
    color: var(--red);
    text-shadow:
      -4px 3px 0 var(--pink),
      2px 2px 0 var(--red-deep);
  }
  .net-weight {
    position: absolute;
    left: 0;
    width: 100%;
    top: 560px;
    margin: 0;
    text-align: center;
    font-family: "Archivo", sans-serif;
    font-weight: 700;
    font-size: 22px;
    color: var(--ink);
  }
  .wave-band {
    position: absolute;
    left: 0;
    bottom: 0;
    width: 650px;
    height: 180px;
  }
</style>
</head>
<body>
<div class="canvas">
  <div class="label">
    <svg class="pepper-arc" viewBox="0 0 500 250" role="img" aria-label="Half-ring filled with a line-drawn chili pepper pattern">
      <defs>
        <linearGradient id="arcFill" x1="0" y1="0" x2="1" y2="0">
          <stop offset="0" stop-color="#f07f86"/>
          <stop offset="0.5" stop-color="#e2474e"/>
          <stop offset="1" stop-color="#d93339"/>
        </linearGradient>
      </defs>
      <path d="M0 0 A250 250 0 0 0 500 0 L370 0 A120 120 0 0 1 130 0 Z" fill="url(#arcFill)"/>
    </svg>

    <h1 class="title">ORIGINAL HOT<br>SAUCE</h1>
    <p class="net-weight">NET WT. 5oz (148 ml)</p>

    <svg class="wave-band" viewBox="0 0 650 180" role="img" aria-label="Red band with a flowing contour line pattern">
      <defs>
        <linearGradient id="bandFill" x1="0" y1="0" x2="1" y2="0">
          <stop offset="0" stop-color="#ec6a71"/>
          <stop offset="1" stop-color="#dc3a40"/>
        </linearGradient>
      </defs>
      <path d="M0 10 C120 0 220 20 330 55 C450 92 560 110 650 110 L650 180 L0 180 Z" fill="url(#bandFill)"/>
    </svg>
  </div>
</div>
</body>
</html>
```